Stationary Design (using existing logo)

Stationary (print and electronic version for Word/email), envelope, and fax cover. All companies are part of same family or course so designs can be the same, or essentially the same. Use the logos attached, same font and colors.

Target Market(s)

Real estate professionals. Investors and other property owners. Financial professionals.

Industry/Entity Type

Real Estate

Font styles to use
Serif

Requirements
Must have
• Should be a serious, sophisticated design in colors that match the business cards we uploaded. Design needs to match the color and fonts in the attached business cards. Can use the same design for each company, just change logo and color.
Should not have
• Nothing quirky or cute.

```html
<!DOCTYPE html>
<html lang="en">
<head>
<meta charset="utf-8">
<title>Northgate Property Partners – Stationery</title>
<link rel="stylesheet" href="https://fonts.googleapis.com/css2?family=Crimson+Text:wght@400;600&display=swap">
<style>
  :root {
    --brick: #b0442a;
    --paper: #ffffff;
    --ink: #3a3a3a;
    --silver-light: #ecebe8;
    --silver-dark: #b9b4ad;
    --backdrop: #ffffff;
  }
  * { box-sizing: border-box; margin: 0; padding: 0; }
  html, body { width: 1200px; height: 1000px; overflow: hidden; background: var(--backdrop); }
  body { position: relative; font-family: "Crimson Text", Georgia, serif; color: var(--ink); }

  .sheet { position: absolute; background: var(--paper); border: 1px solid #e4e4e4; }
  .sheet--red { background: var(--brick); border-color: var(--brick); }

  .wordmark { display: flex; align-items: center; gap: 7px; font-weight: 600; color: var(--brick); letter-spacing: 0.5px; white-space: nowrap; }
  .wordmark__square { width: 12px; height: 12px; background: var(--brick); }
  .wordmark--light { color: var(--paper); }
  .wordmark--light .wordmark__square { background: var(--paper); }

  /* Letterhead */
  .letterhead { left: 125px; top: 76px; width: 455px; height: 624px; }
  .letterhead .wordmark { position: absolute; top: 64px; left: 0; right: 0; justify-content: center; font-size: 17px; }
  .letterhead__accent { position: absolute; right: 8px; bottom: 30px; width: 118px; height: 92px;
    background: linear-gradient(90deg, var(--silver-light), var(--silver-dark), var(--silver-light)); opacity: .7; }
  .letterhead__web { position: absolute; bottom: 32px; left: 0; right: 0; text-align: center; font-size: 10px; color: var(--brick); }
  .letterhead__band { position: absolute; left: 0; right: 0; bottom: 0; height: 26px; background: var(--brick);
    color: var(--paper); font-size: 10px; font-weight: 600; text-align: center; line-height: 26px; }

  /* Letterhead reverse */
  .folder { left: 612px; top: 68px; width: 458px; height: 628px; }
  .folder .wordmark { position: absolute; right: 14px; top: 552px; font-size: 17px; }
  .folder__band { position: absolute; left: 0; right: 0; bottom: 6px; height: 28px; background: var(--paper);
    color: var(--brick); font-size: 10px; font-weight: 600; text-align: center; line-height: 28px; }

  /* Envelope front */
  .envelope { left: 140px; top: 782px; width: 450px; height: 160px; }
  .envelope .wordmark { position: absolute; top: 36px; left: 14px; font-size: 14px; }
  .envelope__web { position: absolute; top: 56px; left: 36px; font-size: 10px; color: var(--brick); }
  .envelope__contact { position: absolute; top: 96px; left: 16px; font-size: 8.5px; line-height: 9px; }
  .envelope__address { display: block; font-weight: 600; font-size: 9.5px; line-height: 9px; margin-top: 1px; }
  .envelope__band { position: absolute; left: 0; right: 0; bottom: 0; height: 14px; background: var(--brick); }

  /* Envelope back */
  .envelope-back { left: 622px; top: 764px; width: 453px; height: 166px; }
  .envelope-back .wordmark { position: absolute; right: 40px; top: 126px; font-size: 14px; }
</style>
</head>
<body>

  <section class="sheet letterhead" aria-label="Letterhead">
    <div class="wordmark"><span class="wordmark__square"></span>Northgate Property Partners</div>
    <div class="letterhead__accent" role="img" aria-label="Soft silver brand accent"></div>
    <p class="letterhead__web">www.northgateprop.com</p>
    <p class="letterhead__band">1480 W Harlow Ave., Chicago, IL 60612</p>
  </section>

  <section class="sheet sheet--red folder" aria-label="Letterhead reverse">
    <div class="wordmark wordmark--light"><span class="wordmark__square"></span>Northgate Property Partners</div>
    <p class="folder__band">1480 W Harlow Ave., Chicago, IL 60612</p>
  </section>

  <section class="sheet envelope" aria-label="Envelope front">
    <div class="wordmark"><span class="wordmark__square"></span>Northgate Property Partners</div>
    <p class="envelope__web">www.northgateprop.com</p>
    <p class="envelope__contact">
      555.010.2400<br>
      555.010.2401 (fax)<br>
      555.010.4068(cell)
      <span class="envelope__address">1480 W Harlow Ave.,<br>Chicago, IL 60612</span>
    </p>
    <div class="envelope__band"></div>
  </section>

  <section class="sheet sheet--red envelope-back" aria-label="Envelope back">
    <div class="wordmark wordmark--light"><span class="wordmark__square"></span>Northgate Property Partners</div>
  </section>

</body>
</html>
```